Dental Practice - Smiles Ahead - Harbin Arcade - requires New Patient Flyer

We need a flyer to tell prospecting new patients about a new patient offer in our practice, Themed with black and whitewith a bit of colour, and using black and white stripes if possible.
We want to look empathetic, modern and appeal to adults.
The offer is for a complete comprehensive dental examination including all necessary x-rays with no out of pocket expense

Target Market(s)

adults, in particular 30-60 year olds

Industry/Entity Type

Dental

Font styles to use
Sans Serif

Colors
000000
ffffff
cee9f5

Requirements
Must have
• Smiles Ahead
• We are located in the heart of city Adelaide, along the iconic Harbin Arcade.
• Dentist
• Complete comprehensive dental examination including all necessary x-rays
• with $0 out of pocket expense if you have dental health cover.
• No Health fund? We will do it all for you $95.
• With over 50 years combined experience, Dr Victor Pellowski and Dr Stuart Hollen can offer all areas of dental treatment including Preventative, Whitening, Children, General, Cosmetic, Removal, Sedation and Implants.
• (08) 8490 3367
• reception@brightcrestdental.com.au
• Level 2, 74 Harbin Arcade Adelaide SA 5000
• Please try and include all 3 pictures attached
Nice to have
• Cover Plus with KORVA, Accept all health funds, claim on the spot with MEDTAP
Should not have
• colour red, someone not smiling, someone in pain, photo of bad teeth/smile

```html
<!DOCTYPE html>
<html lang="en">
<head>
<meta charset="utf-8">
<title>Smiles Ahead – New Patient Offer</title>
<link rel="stylesheet" href="https://fonts.googleapis.com/css2?family=Open+Sans:wdth,wght@75..100,400..800&display=swap">
<style>
  :root {
    --ink: #000000;
    --paper: #ffffff;
    --ice: #cee9f5;
    --bg-light: #3a3a3a;
    --bg-dark: #121212;
    --tab-grey: #7b7b7b;
    --tab-grey-dark: #5f5f5f;
    --fund-blue: #1497d4;
    --band: #e6e6e6;
    --band-text: #1e1e1e;
    --muted: #9a9a9a;
  }
  * { box-sizing: border-box; margin: 0; padding: 0; }
  html, body { width: 849px; height: 1200px; overflow: hidden; background: var(--bg-dark); }
  body { font-family: "Open Sans", Arial, sans-serif; color: var(--paper); }

  .flyer {
    position: relative; width: 849px; height: 1200px; overflow: hidden;
    background: radial-gradient(ellipse 90% 70% at 50% 28%, var(--bg-light) 0%, #232323 55%, var(--bg-dark) 100%);
  }

  .brand {
    position: absolute; top: 92px; left: 0; width: 849px; text-align: center;
    font-size: 50px; font-weight: 600; letter-spacing: 0.5px; line-height: 68px; color: var(--paper);
  }
  .brand__role {
    position: absolute; top: 166px; left: 0; width: 849px; text-align: center;
    font-size: 16px; font-weight: 600; letter-spacing: 6px; text-transform: uppercase; color: var(--ice);
  }

  .offer { position: absolute; left: 45px; top: 300px; }
  .offer__kicker { font-size: 35px; font-weight: 700; line-height: 44px; }
  .offer__title { font-size: 71px; font-weight: 700; line-height: 80px; letter-spacing: -0.5px; }
  .offer__detail { font-size: 24px; line-height: 36px; margin-top: 6px; }
  .offer__detail strong { font-weight: 700; }
  .offer__detail .offer__price { font-size: 32px; font-weight: 800; }

  .fund-tab {
    position: absolute; left: 27px; top: 528px; width: 321px; height: 80px;
    padding: 10px 0 0 20px;
    background: linear-gradient(180deg, var(--tab-grey) 0%, var(--tab-grey-dark) 100%);
    box-shadow: 0 8px 14px rgba(0,0,0,0.55);
  }
  .fund-tab__title { font-size: 30px; font-weight: 700; line-height: 34px; }
  .fund-tab__sub { font-size: 18px; line-height: 26px; text-transform: uppercase; }
  .fund-tab__sub strong { font-size: 22px; font-weight: 800; }

  .about {
    position: absolute; left: 47px; top: 636px;
    font-size: 15px; line-height: 22px; font-stretch: 87.5%; white-space: nowrap;
  }
  .about strong { font-weight: 700; }

  .location { position: absolute; left: 47px; top: 784px; font-stretch: 87.5%; }
  .location__lead { font-size: 13.5px; line-height: 18px; }
  .location__city { font-size: 23px; font-weight: 700; line-height: 28px; }
  .location__tail { font-size: 13.5px; line-height: 18px; }

  .fund-badge {
    position: absolute; left: 47px; top: 855px; width: 105px; height: 120px;
    background: var(--fund-blue); border: 2px solid var(--paper);
  }
  .fund-notes {
    position: absolute; left: 162px; top: 922px;
    font-size: 14px; line-height: 19px; font-stretch: 87.5%;
  }

  .mascot {
    position: absolute; left: 440px; top: 612px; width: 360px; height: 392px;
    border-radius: 110px 110px 30px 30px;
    background: linear-gradient(180deg, #f4f6f7 0%, #dfe4e6 40%, #1d8fc4 62%, #0f5f8a 100%);
  }

  .terms {
    position: absolute; left: 752px; top: 920px; width: 140px;
    transform: rotate(-90deg); transform-origin: center;
    font-size: 10px; color: var(--muted); white-space: nowrap;
  }

  .contact-band {
    position: absolute; left: 0; top: 998px; width: 849px; height: 202px;
    background: linear-gradient(180deg, #f1f1f1 0%, var(--band) 100%);
  }
  .contact-band__map {
    position: absolute; left: 500px; top: 0; width: 349px; height: 202px;
    background: linear-gradient(90deg, rgba(230,230,230,0) 0%, #dadada 40%, #d4d4d4 100%);
  }
  .contact { position: absolute; left: 48px; display: flex; align-items: center; color: var(--band-text); }
  .contact svg { flex: none; }
  .contact--address { top: 1041px; font-size: 20px; }
  .contact--address span { margin-left: 22px; }
  .contact--phone { top: 1068px; font-size: 48px; font-weight: 700; letter-spacing: 0.5px; }
  .contact--phone span { margin-left: 18px; }
  .contact--email { top: 1133px; font-size: 25px; }
  .contact--email span { margin-left: 20px; }
</style>
</head>
<body>
<main class="flyer">
  <div class="brand">Smiles Ahead</div>
  <div class="brand__role">Dentist</div>

  <section class="offer">
    <p class="offer__kicker">Complete Comprehensive</p>
    <h1 class="offer__title">Dental Examination</h1>
    <p class="offer__detail">including <strong>All Necessary X-Rays</strong> with <span class="offer__price">$0 out of pocket</span><br>expense if you have dental health cover</p>
  </section>

  <div class="fund-tab">
    <p class="fund-tab__title">No Health fund?</p>
    <p class="fund-tab__sub">We will do it all for <strong>$95</strong></p>
  </div>

  <p class="about">With over 50 years combined experience<br><strong>Dr Victor Pellowski</strong> and <strong>Dr Stuart Hollen</strong> can offer<br>all areas of treatment including <strong>Preventative, General,</strong><br><strong>Children, Whitening, Cosmetic, Removal, Sedation</strong><br>and <strong>Implants.</strong> They also have a wonderful team of<br>gentle hygienists.</p>

  <div class="location">
    <p class="location__lead">We are located in the heart of city</p>
    <p class="location__city">Adelaide</p>
    <p class="location__tail">along the iconic Harbin Arcade.</p>
  </div>

  <div class="fund-badge" role="img" aria-label="Health fund partner badge"></div>
  <p class="fund-notes">Cover Plus with KORVA,<br>Accept all health funds,<br>Claim on the spot with MEDTAP.</p>

  <div class="mascot" role="img" aria-label="Cartoon tooth character holding up a dental x-ray"></div>

  <p class="terms">*Valid for new patients only</p>

  <div class="contact-band">
    <div class="contact-band__map" role="img" aria-label="Street map showing the practice location in Harbin Arcade"></div>
  </div>

  <p class="contact contact--address">
    <svg width="16" height="24" viewBox="0 0 16 24" aria-hidden="true"><path d="M8 0a7 7 0 0 0-7 7c0 5 7 17 7 17s7-12 7-17a7 7 0 0 0-7-7z" fill="#1e1e1e"/><circle cx="8" cy="7" r="2.6" fill="#eeeeee"/></svg>
    <span>Level 2, 74 Harbin Arcade Adelaide SA 5000</span>
  </p>
  <p class="contact contact--phone">
    <svg width="22" height="28" viewBox="0 0 22 28" aria-hidden="true"><path d="M6 2l4 6-3 3c1 4 4 8 8 10l3-3 4 5-4 4C9 26 1 15 2 6z" fill="none" stroke="#1e1e1e" stroke-width="2" stroke-linejoin="round"/></svg>
    <span>(08) 8490 3367</span>
  </p>
  <p class="contact contact--email">
    <svg width="20" height="16" viewBox="0 0 20 16" aria-hidden="true"><rect x="1" y="1" width="18" height="14" fill="none" stroke="#1e1e1e" stroke-width="2"/><path d="M1 1l9 8 9-8M1 15l7-7M19 15l-7-7" fill="none" stroke="#1e1e1e" stroke-width="1.6"/></svg>
    <span>reception@brightcrestdental.com.au</span>
  </p>
</main>
</body>
</html>
```